Simple elegant feminine design - Going out on my own as a Mortgage Broker.
My thoughts are the following details on the Front, middle of the card possibly? Phone and email smaller font than my name?
Marnie Veltrin
Finance Specialist
p: 0438 215 962
e: marnie@veltrinlending.com.au
Bottom of the card
residential / commercial / equipment
I would like the Font in Rose Gold maybe white or black background? or Possibly a stone grey - are you able to do a few options? I'd like them embossed
Then I had an idea as a simple logo as per the attached if you get the idea in my scribble, my initials, capital M attached to a small v that leads/follows into a circle? Thicker Font In Rose Gold, middle of the card at the back.
Very open to ideas though and what colour you think would look better with the Rose Gold.
Thanks so much for your help, I am not very creative and savvy with this stuff :-)
Industry/Entity Type
Finance
Contact Information for Business Card
Marnie Veltrin
p: 0438 215 962
Look and feel

```html
<!DOCTYPE html>
<html lang="en">
<head>
<meta charset="utf-8">
<title>Marnie Veltrin – Business Cards</title>
<link rel="stylesheet" href="https://fonts.googleapis.com/css2?family=Crimson+Pro:wght@400;500&display=swap">
<style>
  :root {
    --backdrop: #1c1c1d;
    --card: #1f1f21;
    --card-edge: #2a2a2d;
    --rose-gold: #d9a48f;
    --rose-light: #f1cdbd;
    --rose-deep: #a8695a;
    --ink-light: #ecebe8;
    --rule: #0e0e0f;
  }
  * { box-sizing: border-box; margin: 0; padding: 0; }
  html, body { width: 1200px; height: 734px; overflow: hidden; }
  body {
    background: var(--backdrop);
    font-family: "Crimson Pro", Georgia, serif;
    display: flex;
    align-items: center;
    justify-content: center;
    gap: 40px;
  }
  .card {
    position: relative;
    width: 540px;
    height: 348px;
    border-radius: 16px;
    background: radial-gradient(ellipse at 50% 40%, #262628 0%, var(--card) 70%);
    box-shadow: 0 0 0 1px var(--card-edge), 0 14px 30px rgba(0,0,0,.45);
    overflow: hidden;
    text-align: center;
  }

  /* Back: mark + services */
  .brand {
    position: absolute;
    top: 92px; left: 0; right: 0;
    display: flex;
    flex-direction: column;
    align-items: center;
    gap: 14px;
  }
  .brand-circle {
    width: 62px; height: 62px;
    border-radius: 50%;
    border: 2px solid var(--rose-gold);
  }
  .brand-name {
    font-size: 30px;
    font-weight: 500;
    color: var(--rose-gold);
    letter-spacing: .02em;
  }
  .card-back .services { top: 274px; }

  /* Front: name + contact */
  .holder-name {
    position: absolute;
    top: 106px; left: 0; right: 0;
    font-size: 34px;
    font-weight: 500;
    line-height: 1;
  }
  .holder-name span {
    background: linear-gradient(180deg, var(--rose-light) 0%, var(--rose-gold) 55%, var(--rose-deep) 100%);
    -webkit-background-clip: text;
    background-clip: text;
    color: transparent;
    border-bottom: 2px solid var(--rose-gold);
    padding-bottom: 1px;
  }
  .holder-role {
    position: absolute;
    top: 166px; left: 0; right: 0;
    font-size: 18px;
    color: var(--rose-gold);
  }
  .contact {
    position: absolute;
    top: 238px; left: 0; right: 0;
    list-style: none;
    font-size: 13.5px;
    line-height: 23px;
    color: var(--ink-light);
  }
  .contact li { display: flex; align-items: center; justify-content: center; gap: 4px; }
  .contact svg { width: 11px; height: 11px; fill: var(--ink-light); }
  .front-rule {
    position: absolute;
    left: 0; right: 0; top: 305px;
    height: 1px;
    background: var(--rule);
    box-shadow: 0 1px 0 #303033;
  }
  .card-front .services { top: 315px; }

  .services {
    position: absolute;
    left: 0; right: 0;
    font-size: 14.5px;
    color: var(--ink-light);
  }
  .services .dot {
    display: inline-block;
    width: 4px; height: 4px;
    background: var(--ink-light);
    transform: rotate(45deg);
    margin: 0 4px 2px;
  }
</style>
</head>
<body>

  <section class="card card-back" aria-label="Card back">
    <div class="brand">
      <div class="brand-circle"></div>
      <p class="brand-name">Marnie Veltrin</p>
    </div>
    <p class="services">residential<span class="dot"></span>commercial<span class="dot"></span>equipment</p>
  </section>

  <section class="card card-front" aria-label="Card front">
    <h1 class="holder-name"><span>Marnie Veltrin</span></h1>
    <p class="holder-role">Finance Specialist</p>
    <ul class="contact">
      <li>
        <svg viewBox="0 0 24 24" aria-hidden="true"><path d="M6.6 10.8a15.1 15.1 0 0 0 6.6 6.6l2.2-2.2c.3-.3.7-.4 1-.2 1.1.4 2.3.6 3.6.6.6 0 1 .4 1 1V20c0 .6-.4 1-1 1A17 17 0 0 1 3 4c0-.6.4-1 1-1h3.5c.6 0 1 .4 1 1 0 1.3.2 2.5.6 3.6.1.3 0 .7-.2 1z"/></svg>
        0438 215 962
      </li>
      <li>
        <svg viewBox="0 0 24 24" aria-hidden="true"><path d="M3 5h18a1 1 0 0 1 1 1v12a1 1 0 0 1-1 1H3a1 1 0 0 1-1-1V6a1 1 0 0 1 1-1zm1 2.2V17h16V7.2l-8 5.3z"/></svg>
        marnie@veltrinlending.com.au
      </li>
    </ul>
    <div class="front-rule"></div>
    <p class="services">residential<span class="dot"></span>commercial<span class="dot"></span>equipment</p>
  </section>

</body>
</html>
```